Young Architect Bussiness Card

English is not my first language (spanish is).
Need a bussiness card design for my best friend who is about to graduate from college, Licentiate degree in architecture, so she needs business cards to start networking, currently she has no porfolio, web page or facebook. so she is relying on her cel phone and gmail, but should leave space for one of them (facebook)

Design for business card should be modern, maybe something with construction blue prints patern or 3D modelling.

Name: Mariela Fonseca Arrieta
Licentiate in Arquitecture
Cel: (506) XXX-4827
email: marielaXXX@correovela.com

Services, although im not sure if it has to be there or not:
Anteproyectos / Proposal design
Inspecciones / Site Inspections
Modelado 3D / 3D modelling
Planos Constructivos / Construction Blue Prints
Presupuestos / Budgets

Design should be in spanish

Contact Information for Business Card

Name: Mariela Fonseca, Arquitecto
Associtation code : XXXX
Phone: (506) XXXX-XXXX
Email: xxx@correovela.com
Facebook: xxxx

Requirements
Must have
• Design for business card should be modern, maybe something with construction blue prints patern or 3D modelling.
Nice to have
• Something like a transition from 2D to 3D.

```html
<!DOCTYPE html>
<html lang="es">
<head>
<meta charset="utf-8">
<title>Tarjeta de presentación – Mariela Fonseca Arrieta</title>
<link rel="stylesheet" href="https://fonts.googleapis.com/css2?family=Open+Sans:wght@400;600&family=Old+Standard+TT:wght@700&display=swap">
<style>
  :root {
    --page-bg: #e6e2de;
    --card-white: #ffffff;
    --card-lavender: #f0f0fb;
    --ink: #111111;
    --name-blue: #2f3a9e;
    --line-blue: #c9dbe4;
    --wire-tone-a: #f4f9fb;
    --wire-tone-b: #dbe8ee;
    --tool-tone: #b9c2c8;
    --render-tone-a: #dfe3f2;
    --render-tone-b: #eef0fa;
    --shadow: rgba(60, 50, 40, 0.22);
  }
  * { box-sizing: border-box; margin: 0; padding: 0; }
  html, body {
    width: 1200px; height: 864px; overflow: hidden;
    background: var(--page-bg);
  }
  .sheet {
    width: 1200px; height: 864px;
    display: flex; align-items: center; justify-content: center; gap: 40px;
  }
  .card {
    position: relative;
    width: 540px; height: 309px;
    overflow: hidden;
    box-shadow: 0 6px 18px var(--shadow);
  }

  /* Back: services */
  .card--services { background: var(--card-lavender); }
  .services__render {
    position: absolute; left: 0; bottom: 0; width: 300px; height: 230px;
    background: radial-gradient(ellipse at 40% 55%, var(--render-tone-a), var(--render-tone-b) 70%, transparent 100%);
  }
  .services__list {
    position: absolute; left: 44px; top: 58px;
    list-style: none;
    font-family: "Old Standard TT", "Times New Roman", serif;
    font-weight: 700; font-size: 25px; line-height: 38px; color: var(--ink);
  }
  .services__extra {
    position: absolute; left: 330px; top: 96px;
    list-style: none;
    font-family: "Old Standard TT", "Times New Roman", serif;
    font-weight: 700; font-size: 25px; line-height: 38px; color: var(--ink);
  }
  .services__extra li::before { content: "-  "; }

  /* Front: identity */
  .card--identity { background: var(--card-white); }
  .identity__wireframe {
    position: absolute; inset: 0;
    background: linear-gradient(135deg, var(--wire-tone-a) 0%, var(--card-white) 40%, var(--wire-tone-b) 100%);
  }
  .identity__grid { position: absolute; inset: 0; }
  .identity__tool {
    position: absolute; left: 190px; top: 60px; width: 110px; height: 190px;
    background: linear-gradient(160deg, var(--tool-tone), rgba(185,194,200,0.25));
    border-radius: 50px 50px 6px 6px;
    opacity: 0.75;
  }
  .identity__name {
    position: absolute; left: 36px; top: 78px;
    font-family: "Open Sans", Arial, sans-serif;
    font-weight: 400; font-size: 25px; color: var(--name-blue);
  }
  .identity__title {
    position: absolute; left: 38px; top: 114px;
    font-family: "Open Sans", Arial, sans-serif;
    font-size: 15px; color: var(--ink);
  }
  .identity__contact {
    position: absolute; left: 300px; top: 190px;
    list-style: none;
    font-family: "Open Sans", Arial, sans-serif;
    font-size: 15px; line-height: 24px; color: var(--ink);
  }
  .identity__contact li { display: flex; align-items: center; gap: 8px; }
  .contact__icon { width: 14px; height: 14px; flex: none; }
  .contact__spacer { display: inline-block; width: 22px; }
</style>
</head>
<body>
<main class="sheet">

  <section class="card card--services" aria-label="Reverso: servicios">
    <div class="services__render" role="img" aria-label="Render 3D tenue de una casa moderna con un automóvil"></div>
    <ul class="services__list">
      <li>Anteproyectos</li>
      <li>Inspecciones</li>
      <li>Modelado 3D</li>
      <li>Planos Constructivos</li>
      <li>Presupuestos</li>
    </ul>
    <ul class="services__extra">
      <li>Proyectos</li>
      <li>Supervisión</li>
      <li>Remodelación</li>
    </ul>
  </section>

  <section class="card card--identity" aria-label="Frente: datos de contacto">
    <div class="identity__wireframe" role="img" aria-label="Dibujo de líneas arquitectónicas en perspectiva, estilo plano de construcción"></div>
    <svg class="identity__grid" width="540" height="309" viewBox="0 0 540 309" aria-hidden="true">
      <g stroke="var(--line-blue)" stroke-width="1" fill="none">
        <line x1="0" y1="60" x2="540" y2="60"/>
        <line x1="0" y1="250" x2="540" y2="250"/>
        <line x1="120" y1="0" x2="120" y2="309"/>
        <line x1="430" y1="0" x2="430" y2="309"/>
      </g>
      <line x1="250" y1="230" x2="360" y2="110" stroke="#e7a07a" stroke-width="1"/>
    </svg>
    <div class="identity__tool" role="img" aria-label="Compás de dibujo técnico"></div>

    <h1 class="identity__name">Mariela Fonseca Arrieta</h1>
    <p class="identity__title">Licentiate in Arquitecture</p>

    <ul class="identity__contact">
      <li>
        <svg class="contact__icon" viewBox="0 0 14 14" aria-hidden="true">
          <rect width="14" height="14" rx="2" fill="var(--ink)"/>
          <path d="M4 3.5c-.8 1.8.9 5.4 3.5 6.8l1.4-1.3 1.6 1-.8 1.4C6.3 11.6 2.3 7.4 2.8 4.4z" fill="#fff"/>
        </svg>
        (506) XXX-4827
      </li>
      <li>
        <svg class="contact__icon" viewBox="0 0 14 14" aria-hidden="true">
          <rect width="14" height="14" rx="2" fill="var(--ink)"/>
          <rect x="2.5" y="4" width="9" height="6" fill="none" stroke="#fff" stroke-width="1"/>
          <path d="M2.5 4l4.5 3.5L11.5 4" fill="none" stroke="#fff" stroke-width="1"/>
        </svg>
        marielaXXX@correovela.com
      </li>
      <li><span class="contact__spacer"></span>Associtation code : XXXX</li>
      <li><span class="contact__spacer"></span>Facebook: xxxx</li>
    </ul>
  </section>

</main>
</body>
</html>
```